Building Company Business Card Design

I am looking to get a business card designed for my Building Company. Please find the logo attached.

Industry/Entity Type

Business

Contact Information for Business Card

Mobile 0472 913 706
Email admin@harbourlineconstruct.com.au
Website www.harbourlineconstruct.com.au

Colors
0255a3

```html
<!DOCTYPE html>
<html lang="en">
<head>
<meta charset="utf-8">
<title>Harbourline Construct — Business Card</title>
<link rel="stylesheet" href="https://fonts.googleapis.com/css2?family=Arimo:wght@400;700&display=swap">
<style>
  :root {
    --brand-blue: #0255a3;
    --band-white: #ffffff;
    --base-grey: #c4c4c4;
    --card-black: #1e1e1e;
    --ink: #1c1c1c;
    --ink-soft: #3a3a3a;
    --backdrop: #2e2826;
    --logo-grey: #8a8a8a;
  }
  * { box-sizing: border-box; margin: 0; padding: 0; }
  html, body {
    width: 1200px; height: 810px; overflow: hidden;
    background: var(--backdrop);
    font-family: "Arimo", Arial, sans-serif;
  }
  .canvas { position: relative; width: 1200px; height: 810px; }

  .card {
    position: absolute;
    width: 520px; height: 300px;
    border-radius: 18px;
    overflow: hidden;
    box-shadow: 0 14px 30px rgba(0,0,0,.45);
  }

  /* Back side */
  .card--back {
    left: 60px; top: 120px;
    background: var(--card-black);
    display: flex; align-items: center; justify-content: center;
  }
  .card--back .brand-name { color: var(--brand-blue); }

  .brand {
    display: flex; align-items: center; gap: 12px;
  }
  .brand-mark {
    width: 14px; height: 14px; border-radius: 50%;
    background: currentColor;
  }
  .brand-name {
    font-weight: 700;
    font-size: 34px;
    letter-spacing: .5px;
    line-height: 1;
  }

  /* Front side */
  .card--front {
    left: 620px; top: 390px;
    background: var(--base-grey);
  }
  .front-top {
    position: absolute; left: 0; top: 0;
    width: 100%; height: 120px;
    background: var(--brand-blue);
    display: flex; align-items: center; justify-content: center;
    padding-left: 90px;
  }
  .front-top .brand { color: var(--band-white); }
  .front-top .brand-name { color: var(--band-white); font-size: 30px; }
  .front-band {
    position: absolute; left: 0; top: 120px;
    width: 100%; height: 44px;
    background: var(--band-white);
  }
  .holder {
    position: absolute; left: 0; top: 150px;
    width: 100%;
    padding-left: 90px;
    text-align: center;
  }
  .holder-name { font-size: 19px; color: var(--ink); }
  .holder-role { font-size: 15px; color: var(--brand-blue); margin-top: 2px; }

  .contact {
    position: absolute; left: 0; top: 210px;
    width: 100%;
    padding-left: 60px;
    text-align: center;
    list-style: none;
    font-size: 15px; line-height: 21px;
    color: var(--ink-soft);
  }
</style>
</head>
<body>
<main class="canvas">
  <section class="card card--back" aria-label="Business card back">
    <div class="brand">
      <span class="brand-name">Harbourline Construct</span>
    </div>
  </section>

  <section class="card card--front" aria-label="Business card front">
    <header class="front-top">
      <div class="brand">
        <span class="brand-name">Harbourline Construct</span>
      </div>
    </header>
    <div class="front-band"></div>
    <div class="holder">
      <p class="holder-name">Sample Name</p>
      <p class="holder-role">Owner</p>
    </div>
    <ul class="contact">
      <li>0472 913 706</li>
      <li>admin@harbourlineconstruct.com.au</li>
      <li>www.harbourlineconstruct.com.au</li>
    </ul>
  </section>
</main>
</body>
</html>
```